Sunridge Beacon Wholesale Business Card Design

Use logo and expand the framing box to the extents of the business card. Keep company name in right bottom corner and triangle at top right corner. I would like to have a template so that I can fill in employee name, contact info, email and website.

```html
<!DOCTYPE html>
<html lang="en">
<head>
<meta charset="utf-8">
<title>Sunridge Beacon Wholesale – Business Card</title>
<link href="https://fonts.googleapis.com/css2?family=Bebas+Neue&display=swap" rel="stylesheet">
<style>
  :root{
    --ink:#000000;
    --paper:#ffffff;
    --brand-blue:#0a82c8;
    --backdrop:#3b3b3b;
    --frame:7px;
  }
  *{margin:0;padding:0;box-sizing:border-box}
  html,body{width:1200px;height:689px;overflow:hidden}
  body{background:var(--backdrop);position:relative;font-family:"Bebas Neue",Impact,sans-serif;color:var(--ink)}
  .card{position:absolute;width:520px;height:297px;overflow:hidden;box-shadow:0 12px 30px rgba(0,0,0,.45)}
  .card--front{left:50px;top:60px;background:var(--paper)}
  .card--back{left:630px;top:330px;background:var(--brand-blue)}
  .rule{position:absolute;background:var(--ink)}
  .corner-triangle{position:absolute;left:0;top:0;width:520px;height:297px}

  .company-name{position:absolute;left:48px;top:96px;font-size:64px;line-height:58px;letter-spacing:1px;text-transform:uppercase;font-weight:400;white-space:nowrap}

  .person{position:absolute;left:62px;top:148px;white-space:nowrap}
  .person__name{font-size:44px;line-height:40px;letter-spacing:.5px;font-weight:400}
  .person__title{font-size:24px;line-height:22px;margin-left:52px}

  .contact{position:absolute;left:296px;top:100px;list-style:none;font-size:14px;line-height:16px;letter-spacing:.3px;white-space:nowrap}
  .contact li{display:flex;align-items:flex-start;gap:8px;margin-bottom:3px}
  .contact svg{width:11px;height:11px;flex:none;margin-top:2px}
</style>
</head>
<body>

<section class="card card--front" aria-label="Card front">
  <svg class="corner-triangle" viewBox="0 0 520 297" aria-hidden="true">
    <polygon points="368,56 458,8 500,64" fill="#0a82c8"/>
  </svg>
  <div class="rule" style="left:28px;top:54px;width:342px;height:var(--frame)"></div>
  <div class="rule" style="left:28px;top:54px;width:var(--frame);height:70px"></div>
  <div class="rule" style="left:486px;top:72px;width:var(--frame);height:180px"></div>
  <div class="rule" style="left:382px;top:245px;width:111px;height:var(--frame)"></div>
  <h1 class="company-name">Sunridge<br>Beacon<br>Wholesale</h1>
</section>

<section class="card card--back" aria-label="Card back">
  <svg class="corner-triangle" viewBox="0 0 520 297" aria-hidden="true">
    <polygon points="338,58 430,10 476,66" fill="#ffffff"/>
  </svg>
  <div class="rule" style="left:28px;top:56px;width:300px;height:var(--frame)"></div>
  <div class="rule" style="left:28px;top:56px;width:var(--frame);height:212px"></div>
  <div class="rule" style="left:486px;top:74px;width:var(--frame);height:194px"></div>
  <div class="rule" style="left:28px;top:261px;width:465px;height:var(--frame)"></div>

  <div class="person">
    <h2 class="person__name">Daniel Reyes</h2>
    <p class="person__title">Founder &amp; CEO</p>
  </div>

  <ul class="contact">
    <li>
      <svg viewBox="0 0 12 12"><path d="M6 0a4 4 0 0 0-4 4c0 3 4 8 4 8s4-5 4-8a4 4 0 0 0-4-4zm0 5.5A1.5 1.5 0 1 1 6 2.5a1.5 1.5 0 0 1 0 3z" fill="#000"/></svg>
      <span>Your Address, City<br>State, Country, Zip 1235</span>
    </li>
    <li>
      <svg viewBox="0 0 12 12"><path d="M2 1l2.5 0 1 3-1.5 1a7 7 0 0 0 3 3l1-1.5 3 1V10a1 1 0 0 1-1 1A9 9 0 0 1 1 2a1 1 0 0 1 1-1z" fill="#000"/></svg>
      <span>(123) 456-7890</span>
    </li>
    <li>
      <svg viewBox="0 0 12 12"><rect x="3" y="0.5" width="6" height="11" rx="1" fill="none" stroke="#000" stroke-width="1.3"/><circle cx="6" cy="9.5" r=".8" fill="#000"/></svg>
      <span>(123) 456-7890</span>
    </li>
    <li>
      <svg viewBox="0 0 12 12"><rect x="0.5" y="2" width="11" height="8" fill="#000"/><path d="M0.5 2l5.5 4.5L11.5 2" fill="none" stroke="#0a82c8" stroke-width="1"/></svg>
      <span>daniel@yourwebsite.com</span>
    </li>
    <li>
      <svg viewBox="0 0 12 12"><circle cx="6" cy="6" r="5.2" fill="none" stroke="#000" stroke-width="1.3"/><path d="M1 6h10M6 1c-2.5 3-2.5 7 0 10M6 1c2.5 3 2.5 7 0 10" fill="none" stroke="#000" stroke-width="1"/></svg>
      <span>www.yourwebsite.com</span>
    </li>
  </ul>
</section>

</body>
</html>
```